Sol Gorditas Digital Menu Boards

IF SELECTED, WINNER MAY BE HIRED FOR OTHER DESIGNS OF DIFFERENT STORES OF OUR COMPANY.

Task: Digital Menu Boards Design

Task description: We need designs for a Digital Menu to be displayed on two 42’’screens at Solgorditas, a fast-food restaurant in Guadalajara, Mexico. The menu redesign should communicate to our customers the experience of eating at our restaurant.

For avoiding the creation of videos, we are expecting several menu slides with the same text but with different images, simulating the effect of a video where the images are changing. This menu slides will be projected through a USB memory and a slideshow.

Attached files:
For the design, there are several documents attached to the task description:
1. Logo of the restaurant
2. Pictures of the restaurant
3. Example video of what we want to achieve through this menu slides.
4. Pictures of the actual menu board, to be replaced with the new designs.
5. Menu description (regular and breakfast menu)
6. Pictures of each element on the menu (We don’t have yet any breakfast pictures)
**The files are organized on a ZIP file.

Expected product:
For the regular menu,
• 2 menu slide designs for TACOS Y ESPECIALIDADES, where the text will be exactly the same but the images would differ.
• 2 menu slide designs for BEBIDAS Y EXTRAS, where the text will be exactly the same but the images would differ.
For the breakfast menu,
• 1 menu slide including all the menu
Total: 5 menu board slides.

Technical specs:
• You should send the editable file, med and high resolution JPGs for each design.
• The designs should fit perfectly on 42’’ screens.

```html
<!DOCTYPE html>
<html lang="es">
<head>
<meta charset="utf-8">
<title>Sol Gorditas – Menú digital</title>
<link href="https://fonts.googleapis.com/css2?family=Arimo:wght@700&display=swap" rel="stylesheet">
<style>
  :root {
    --cream: #f3ead7;
    --red: #d9301f;
    --dark-red: #b3241a;
    --black: #111111;
    --white: #ffffff;
    --photo-warm: #c98a5a;
    --photo-deep: #8a5a3a;
  }
  * { box-sizing: border-box; margin: 0; padding: 0; }
  html, body { width: 900px; height: 1200px; overflow: hidden; }
  body { font-family: "Arimo", Arial, sans-serif; font-weight: 700; background: var(--white); position: relative; }

  .screen { position: absolute; left: 0; width: 900px; background: var(--cream); overflow: hidden; }
  .screen--one { top: 0; height: 525px; }
  .screen--two { top: 630px; height: 570px; }
  .top-edge { position: absolute; top: 0; left: 0; width: 100%; height: 36px; background: var(--red); }
  .ground { position: absolute; left: 0; bottom: 0; width: 100%; height: 75px; background: var(--black); }

  .brand { position: absolute; display: flex; align-items: center; gap: 10px; color: var(--red); font-size: 30px; }
  .brand__dot { width: 34px; height: 34px; border-radius: 50%; background: var(--red); flex: none; }
  .screen--one .brand { left: 24px; top: 62px; }
  .screen--two .brand { left: 340px; top: 1000px; top: 372px; }

  .menu-title { position: absolute; top: 160px; left: 240px; width: 420px; text-align: center; font-size: 26px; color: var(--black); }
  .col-head, .cell { position: absolute; width: 150px; text-align: center; }
  .col-head { top: 208px; font-size: 24px; color: var(--black); }
  .price-band { position: absolute; left: 0; top: 243px; width: 100%; height: 117px; background: var(--red); }
  .row-label { position: absolute; left: 14px; font-size: 30px; color: var(--white); }
  .cell { font-size: 28px; color: var(--white); }
  .tortilla-band { position: absolute; left: 0; top: 375px; width: 100%; height: 70px; background: var(--black); }
  .tortilla-band .row-label, .tortilla-band .cell { top: 20px; font-size: 24px; }

  .divider { position: absolute; top: 525px; left: 0; width: 900px; height: 105px; display: flex; align-items: center; justify-content: space-between; padding: 0 20px; color: var(--red); }
  .divider__side { font-size: 36px; }
  .divider__menu { font-size: 58px; display: flex; align-items: center; gap: 16px; }
  .divider__line { width: 110px; height: 4px; background: var(--red); }

  .dish-label { position: absolute; font-size: 38px; color: var(--black); }
  .dish-label--red { color: var(--red); }
  .dish-photo { position: absolute; border: 6px solid var(--dark-red); background: linear-gradient(135deg, var(--photo-warm), var(--photo-deep)); }
</style>
</head>
<body>
  <section class="screen screen--one">
    <div class="top-edge"></div>
    <div class="brand"><span class="brand__dot"></span>Sol Gorditas</div>
    <h1 class="menu-title">TACOS Y ESPECIALIDADES</h1>
    <div class="col-head" style="left:300px">Tacos</div>
    <div class="col-head" style="left:450px">Quesadilla</div>
    <div class="col-head" style="left:625px">Volcán</div>
    <div class="col-head" style="left:750px">Gringa</div>
    <div class="price-band">
      <div class="row-label" style="top:14px">Pastor:</div>
      <div class="cell" style="left:300px;top:14px">14</div>
      <div class="cell" style="left:450px;top:14px">18</div>
      <div class="cell" style="left:625px;top:14px">18</div>
      <div class="cell" style="left:750px;top:14px">20</div>
      <div class="row-label" style="top:66px">Arrachera</div>
      <div class="cell" style="left:300px;top:66px">16</div>
      <div class="cell" style="left:450px;top:66px">20</div>
      <div class="cell" style="left:625px;top:66px">20</div>
    </div>
    <div class="tortilla-band">
      <div class="row-label">Tortilla de Harina</div>
      <div class="cell" style="left:300px">+1</div>
      <div class="cell" style="left:450px">+ 1</div>
      <div class="cell" style="left:625px">+ 1</div>
      <div class="cell" style="left:750px">+2</div>
    </div>
    <div class="ground" role="img" aria-label="Silueta de pasto y nopales"></div>
  </section>

  <div class="divider">
    <span class="divider__side">SCREEN 1</span>
    <span class="divider__menu"><span class="divider__line"></span>MENU<span class="divider__line"></span></span>
    <span class="divider__side">SCREEN 2</span>
  </div>

  <section class="screen screen--two">
    <div class="top-edge"></div>
    <div class="dish-label" style="left:186px;top:70px">Tacos</div>
    <div class="dish-label" style="left:470px;top:70px">Quesadillas</div>
    <div class="dish-photo" role="img" aria-label="Foto de tacos con salsa" style="left:186px;top:125px;width:258px;height:160px"></div>
    <div class="dish-photo" role="img" aria-label="Foto de quesadillas" style="left:450px;top:125px;width:255px;height:160px"></div>
    <div class="dish-label dish-label--red" style="left:20px;top:168px">Volcan</div>
    <div class="dish-label dish-label--red" style="left:760px;top:168px">Gringa</div>
    <div class="dish-photo" role="img" aria-label="Foto de volcanes con carne" style="left:15px;top:220px;width:234px;height:160px"></div>
    <div class="dish-photo" role="img" aria-label="Foto de gringa en plato" style="left:630px;top:225px;width:255px;height:180px"></div>
    <div class="brand"><span class="brand__dot"></span>Sol Gorditas</div>
    <div class="ground" role="img" aria-label="Silueta de pasto y nopales"></div>
  </section>
</body>
</html>
```